Net Clarity Partners Needs a New Business Card Design

Attached is my new logo that ArtFlockly created and picture of me for the back of the business card. Also attached is the information to include on the business card (on my existing business card design - NCP1 file attached).

The designer also provided a treatment of my logo that I really like if you can use it somehow. Also attached - file name "Preferred Version of New Logo."

Marla Quinteros

Net Clarity Partners
4817 Brindle Ave., #315
Houston, TX 77056

Tel: (832) 555-0147
www.netclaritypartners.example
marla@netclaritypartners.example

Thank you.

Target Market(s)

attorneys and law firms

Industry/Entity Type

Legal

Contact Information for Business Card

Proved in the Project Description

Font styles to use
Other font styles liked:
• I am open on font - no script though.

Colors
2d73b3
33a6d7

Requirements
Must have
• my logo
• company name & contact info
• my picture on the back
• colors that coordinate with the logo
Nice to have
• love to use the treated version of the logo if possible

```html
<!DOCTYPE html>
<html lang="en">
<head>
<meta charset="utf-8">
<title>Net Clarity Partners – Business Card</title>
<link rel="stylesheet" href="https://fonts.googleapis.com/css2?family=Open+Sans:wght@400;600;700&display=swap">
<style>
  :root {
    --brand-blue: #2ba6e1;
    --brand-grey: #939598;
    --text-grey: #666a6e;
    --rule-grey: #9a9a9a;
    --card-white: #ffffff;
    --backdrop: #e9eaec;
    --photo-light: #a9a9ab;
    --photo-dark: #6e6a70;
  }
  * { margin: 0; padding: 0; box-sizing: border-box; }
  html, body {
    width: 1200px; height: 1000px; overflow: hidden;
    background: var(--backdrop);
    font-family: "Open Sans", Arial, sans-serif;
  }
  .canvas { position: relative; width: 1200px; height: 1000px; }

  .card {
    position: absolute; left: 266px; width: 666px; height: 397px;
    overflow: hidden;
    box-shadow: 0 2px 8px rgba(0,0,0,0.18);
  }
  .card--front { top: 74px; background: var(--card-white); }
  .card--back { top: 534px; background: var(--brand-blue); }

  .company {
    position: absolute; display: flex; align-items: center; gap: 12px;
    font-weight: 700; text-transform: uppercase; white-space: nowrap;
  }
  .card--front .company {
    left: 34px; top: 118px; font-size: 24px; color: var(--brand-blue); letter-spacing: 0.3px;
  }
  .company__dot {
    width: 22px; height: 22px; border-radius: 50%; background: currentColor; flex: none;
  }

  .portrait {
    position: absolute; left: 488px; top: 52px; width: 146px; height: 146px;
    border-radius: 50%; border: 3px solid var(--brand-blue);
    background: var(--card-white); padding: 3px;
  }
  .portrait__fill {
    width: 100%; height: 100%; border-radius: 50%;
    background: radial-gradient(circle at 50% 40%, var(--photo-light), var(--photo-dark));
  }

  .person { position: absolute; right: 33px; top: 204px; text-align: right; }
  .person__name { font-size: 24px; font-weight: 600; color: var(--brand-blue); line-height: 32px; }
  .person__title { font-size: 16px; color: var(--text-grey); line-height: 20px; }

  .rule {
    position: absolute; left: 32px; top: 244px; width: 450px; height: 2px; background: var(--rule-grey);
  }

  .contacts { position: absolute; left: 32px; top: 274px; list-style: none; }
  .contacts li {
    display: flex; align-items: center; gap: 8px;
    font-size: 16px; color: var(--text-grey); line-height: 24px;
  }
  .contacts svg { width: 15px; height: 15px; fill: var(--brand-blue); flex: none; }

  .address {
    position: absolute; right: 33px; top: 297px; text-align: right;
    font-size: 16px; color: var(--text-grey); line-height: 23px; font-style: normal;
  }

  .band { position: absolute; left: 0; bottom: 0; width: 666px; height: 26px; }

  .card--back .company {
    left: 0; right: 0; top: 200px; justify-content: center;
    font-size: 30px; color: var(--card-white); letter-spacing: 0.5px;
  }
</style>
</head>
<body>
<main class="canvas">

  <section class="card card--front" aria-label="Card front">
    <div class="company"><span class="company__dot"></span>Net Clarity Partners</div>

    <div class="portrait"><div class="portrait__fill" role="img" aria-label="Portrait photo of Marla Quinteros"></div></div>

    <div class="person">
      <p class="person__name">Marla Quinteros</p>
      <p class="person__title">Managing Director</p>
    </div>

    <div class="rule"></div>

    <ul class="contacts">
      <li>
        <svg viewBox="0 0 16 16" aria-hidden="true"><path d="M3 3h10c1 0 2 1 2 2v1h-4V5H5v1H1V5c0-1 1-2 2-2zm1 4h8l3 5v2H1v-2zm4 2a2 2 0 100 4 2 2 0 000-4z"/></svg>
        (832) 555-0147
      </li>
      <li>
        <svg viewBox="0 0 16 16" aria-hidden="true"><path d="M1 3h14v10H1zm1.5 1.5L8 9l5.5-4.5v-.2h-11z" fill-rule="evenodd"/></svg>
        marla@netclaritypartners.example
      </li>
      <li>
        <svg viewBox="0 0 16 16" aria-hidden="true"><path d="M8 1a7 7 0 100 14A7 7 0 008 1zm0 2a5 5 0 014.6 3H9.5L8 4.5 6 6H3.4A5 5 0 018 3zm-5 5h3l2 2v3a5 5 0 01-5-5zm7 4.6V10l2-2h1a5 5 0 01-3 4.6z"/></svg>
        www.netclaritypartners.example
      </li>
    </ul>

    <address class="address">
      4817 Brindle Ave., #315<br>
      Houston, TX 77056
    </address>

    <svg class="band" viewBox="0 0 666 26" preserveAspectRatio="none" aria-hidden="true">
      <polygon points="0,2 338,2 362,26 0,26" fill="var(--brand-blue)"/>
      <polygon points="346,0 666,0 666,26 372,26" fill="var(--brand-grey)"/>
    </svg>
  </section>

  <section class="card card--back" aria-label="Card back">
    <div class="company">Net Clarity Partners</div>
  </section>

</main>
</body>
</html>
```